Business card to be used as a flyer

This business card should do the trick of a full scale flyer , so basicaly from the business card itself we only keep the size and remove the clasical name , position , company name (etc).
This business cards should be , like said above, used as promo tool, being gived to different girls . So base one : the design is girls oriented.
Colors : black background . We will use gold (color) folio for the text.
Attached you have our logo, but this should not be a proiminent part of the design . You can use only the cat head instead.
Target Market(s)
Girls / Women
Contact Information for Business Card
> black background , gold / folio text and elements
> cat head from the logo in a creative way do be displayed
> proieminent text "your path to success starts here"
> contact details phone and website .
www.velmastrand.ro (website) and 0742163958 (phone)

```html
<!DOCTYPE html>
<html lang="en">
<head>
<meta charset="utf-8">
<title>Velmastrand promo card</title>
<link rel="stylesheet" href="https://fonts.googleapis.com/css2?family=Cormorant+Garamond:ital,wght@0,500;1,500&family=Pinyon+Script&display=swap">
<style>
  :root {
    --card-black: #000000;
    --gold: #d8b46a;
    --gold-soft: rgba(216, 180, 106, 0.55);
    --gold-faint: rgba(216, 180, 106, 0);
  }
  html, body {
    margin: 0;
    padding: 0;
    width: 785px;
    height: 1200px;
    overflow: hidden;
    background: var(--card-black);
  }
  .card {
    position: relative;
    width: 785px;
    height: 1200px;
    background: var(--card-black);
    color: var(--gold);
    font-family: "Cormorant Garamond", Georgia, serif;
    overflow: hidden;
  }
  .glitter-band {
    position: absolute;
    left: 0;
    top: 0;
    width: 785px;
    height: 250px;
    background: linear-gradient(to bottom, var(--gold-soft) 0%, rgba(216,180,106,0.25) 45%, var(--gold-faint) 100%);
  }
  .cat-illustration {
    position: absolute;
    left: 187px;
    top: 118px;
    width: 414px;
    height: 663px;
    background: radial-gradient(ellipse at 55% 45%, rgba(216,180,106,0.45) 0%, rgba(216,180,106,0.15) 60%, rgba(216,180,106,0) 100%);
  }
  .tagline-line {
    position: absolute;
    margin: 0;
    font-style: italic;
    font-weight: 500;
    line-height: 1;
    white-space: nowrap;
  }
  .tagline-your { left: 444px; top: 680px; font-size: 56px; }
  .tagline-path { left: 446px; top: 744px; font-size: 56px; }
  .tagline-success {
    position: absolute;
    left: 88px;
    top: 800px;
    margin: 0;
    font-family: "Pinyon Script", cursive;
    font-weight: 400;
    font-size: 150px;
    line-height: 1;
    white-space: nowrap;
  }
  .tagline-starts { right: 117px; top: 935px; font-size: 60px; }
  .contact {
    position: absolute;
    right: 113px;
    margin: 0;
    display: flex;
    align-items: center;
    gap: 12px;
    font-size: 29px;
    font-weight: 500;
    letter-spacing: 0.5px;
    line-height: 1;
  }
  .contact-web { top: 1040px; }
  .contact-phone { top: 1090px; }
  .contact-icon { width: 20px; height: 20px; }
  .accent-bar {
    position: absolute;
    left: 769px;
    top: 1032px;
    width: 16px;
    height: 91px;
    background: var(--gold);
  }
</style>
</head>
<body>
  <main class="card">
    <div class="glitter-band" role="img" aria-label="Scattered gold glitter across the top of the card"></div>
    <div class="cat-illustration" role="img" aria-label="Gold line illustration of a cat head in profile with a flowing neck curve"></div>

    <p class="tagline-line tagline-your">your</p>
    <p class="tagline-line tagline-path">path to</p>
    <h1 class="tagline-success">Success</h1>
    <p class="tagline-line tagline-starts">starts here</p>

    <p class="contact contact-web">
      <span>www.velmastrand.ro</span>
      <svg class="contact-icon" viewBox="0 0 20 20" aria-hidden="true">
        <rect x="1.5" y="4" width="17" height="12" fill="none" stroke="currentColor" stroke-width="1.6"/>
        <path d="M1.5 4 L10 11 L18.5 4 M1.5 16 L7.5 10 M18.5 16 L12.5 10" fill="none" stroke="currentColor" stroke-width="1.4"/>
      </svg>
    </p>
    <p class="contact contact-phone">
      <span>0742163958</span>
      <svg class="contact-icon" viewBox="0 0 20 20" aria-hidden="true">
        <path d="M5 2.5 L8 6 L6.3 8 C7.3 10.3 9.7 12.7 12 13.7 L14 12 L17.5 15 L15.5 17.5 C9 17 3 11 2.5 4.5 Z" fill="none" stroke="currentColor" stroke-width="1.6" stroke-linejoin="round"/>
        <path d="M11 3.5 A6 6 0 0 1 16.5 9 M11 6.5 A3 3 0 0 1 13.5 9" fill="none" stroke="currentColor" stroke-width="1.4"/>
      </svg>
    </p>

    <div class="accent-bar"></div>
  </main>
</body>
</html>
```